Cornflute Firewood advertising Sign for passing by traffic

900mm W
1200mm H

I am looking for a design to place outside of our nursery to advertise our firewood. We have a lot of traffic passing by and want to capture the eyes of potential customers.

We want a modern sleek look that will set the tone for the product

key things i want to hit -
Visual of firewood or fire
Quality product
we deliver
Clean firewood

Target Market(s)

Older retired people
Young families
Passing traffic

Industry/Entity Type

Firewood

Font styles to use
Serif
Sans Serif

Requirements
Must have
• Great eye catching picture
• colorful
• Easy to read for passers by
• Picture of firewood or fireplace or anything you seem relevant to the sale of firewood
• If using picture of firewood make sure it is Australian hardwood
Should not have
• Phone number or business name

```html
<!DOCTYPE html>
<html lang="en">
<head>
<meta charset="utf-8">
<title>Clean Firewood – Roadside Sign</title>
<link rel="stylesheet" href="https://fonts.googleapis.com/css2?family=Bowlby+One+SC&display=swap">
<style>
  :root {
    --frame-orange: #f7a12e;
    --headline-orange: #e0701e;
    --paper: #ffffff;
    --wood-tan: #c89a68;
    --wood-shadow: #8a2a0c;
    --fire-core: #ffd27a;
    --fire-mid: #f07a1c;
    --brick-dark: #3a0d05;
    --brick-red: #8a2a12;
  }
  html, body {
    margin: 0;
    padding: 0;
    overflow: hidden;
    background: var(--paper);
  }
  .sign {
    position: relative;
    width: 901px;
    height: 1200px;
    box-sizing: border-box;
    border: 14px solid var(--frame-orange);
    background: var(--paper);
    overflow: hidden;
  }
  .sign__art {
    position: absolute;
    inset: 0;
    display: block;
  }
  .headline {
    font-family: "Bowlby One SC", "Arial Black", sans-serif;
    fill: var(--headline-orange);
  }
  .wood-title {
    font-family: "Bowlby One SC", "Arial Black", sans-serif;
  }
  .wood-title__shadow { fill: var(--wood-shadow); }
  .wood-title__face { fill: var(--wood-tan); }
</style>
</head>
<body>
  <main class="sign">
    <svg class="sign__art" width="901" height="1200" viewBox="0 0 901 1200" xmlns="http://www.w3.org/2000/svg">
      <defs>
        <radialGradient id="fireplace-glow" cx="0.5" cy="0.62" r="0.6">
          <stop offset="0" stop-color="var(--fire-core)"/>
          <stop offset="0.25" stop-color="var(--fire-mid)"/>
          <stop offset="0.6" stop-color="var(--brick-red)"/>
          <stop offset="1" stop-color="var(--brick-dark)"/>
        </radialGradient>
      </defs>

      <text class="headline" x="36" y="104" font-size="86" textLength="830" lengthAdjust="spacingAndGlyphs">QUALITY PRODUCT</text>
      <text class="headline" x="182" y="220" font-size="86" textLength="528" lengthAdjust="spacingAndGlyphs">WE DELIVER</text>

      <rect class="fireplace-photo" x="14" y="259" width="873" height="504" fill="url(#fireplace-glow)"
            role="img" aria-label="Photo of hardwood logs burning in a brick fireplace"/>

      <g class="wood-title">
        <text class="wood-title__shadow" x="208" y="948" font-size="180" textLength="446" lengthAdjust="spacingAndGlyphs">CLEAN</text>
        <text class="wood-title__face" x="200" y="940" font-size="180" textLength="446" lengthAdjust="spacingAndGlyphs">CLEAN</text>
        <text class="wood-title__shadow" x="40" y="1089" font-size="180" textLength="830" lengthAdjust="spacingAndGlyphs">FIREWOOD</text>
        <text class="wood-title__face" x="32" y="1081" font-size="180" textLength="830" lengthAdjust="spacingAndGlyphs">FIREWOOD</text>
      </g>
    </svg>
  </main>
</body>
</html>
```